Looking for a new business card design

We are looking for a corporate looking yet still a bit different then the rest. I would like the card black with the picture on the back and the phrase "Leading every crew home SAFE" on the back as well. Then a clean look on the front with a bit of an edge.

Target Market(s)

Corporate oil executives and drilling supervisors

Industry/Entity Type

Oil And Gas

Contact Information for Business Card

Black, bold, clean lines.

Font styles to use
Sans Serif

Requirements
Must have
• Picture on the back with the slogan "Leading every crew home SAFE"
• Black background
• Stands out

```html
<!DOCTYPE html>
<html lang="en">
<head>
<meta charset="utf-8">
<title>Borealis Energy Services – Business Card</title>
<link href="https://fonts.googleapis.com/css2?family=Open+Sans:ital,wght@0,400;0,600;0,700;1,700&display=swap" rel="stylesheet">
<style>
  :root {
    --stage: #e4e4e4;
    --navy: #2f5d8a;
    --lime: #c3cc1c;
    --ink: #4a4a4a;
    --black: #000000;
    --white: #ffffff;
  }
  * { margin: 0; padding: 0; box-sizing: border-box; }
  html, body {
    width: 1200px; height: 987px; overflow: hidden;
    background: var(--stage);
    font-family: "Open Sans", Arial, sans-serif;
  }
  .card {
    position: absolute; left: 293px; width: 615px; height: 352px; overflow: hidden;
    box-shadow: 0 1px 3px rgba(0,0,0,0.25);
  }
  .card-front { top: 130px; background: var(--white); }
  .card-back { top: 505px; background: var(--black); }
  .card-art { position: absolute; inset: 0; width: 100%; height: 100%; }

  .brand {
    position: absolute; left: 50px; top: 122px;
    display: flex; align-items: center; gap: 14px;
  }
  .brand-dot { width: 62px; height: 62px; border-radius: 50%; background: var(--navy); }
  .brand-name {
    color: var(--lime); font-weight: 600; line-height: 1.1;
    font-size: 30px; letter-spacing: 0.5px;
  }
  .brand-name span { display: block; font-size: 15px; letter-spacing: 0; }

  .contact { position: absolute; left: 363px; top: 62px; color: var(--ink); }
  .contact-name { color: var(--navy); font-weight: 700; font-size: 21px; letter-spacing: 0.5px; line-height: 26px; }
  .contact-role { color: var(--lime); font-size: 16px; line-height: 20px; margin-bottom: 10px; }
  .contact-address { font-size: 15px; line-height: 23px; margin-bottom: 8px; }
  .contact-list { list-style: none; font-size: 15px; }
  .contact-list li { display: flex; align-items: center; gap: 9px; height: 23.5px; }
  .contact-list svg { width: 14px; height: 14px; fill: var(--navy); flex: none; }
  .contact-list .web { color: var(--navy); }
</style>
</head>
<body>

<section class="card card-front">
  <svg class="card-art" viewBox="0 0 615 352" preserveAspectRatio="none" aria-hidden="true">
    <path d="M0 0 H615 V40 Q307 0 0 40 Z" fill="var(--navy)"/>
    <path d="M0 40 Q307 0 615 40 Q330 18 0 48 Z" fill="var(--lime)"/>
    <path d="M0 305 Q307 330 615 305 V352 H0 Z" fill="var(--navy)"/>
    <path d="M0 295 Q300 318 615 305 Q307 330 0 305 Z" fill="var(--lime)"/>
  </svg>

  <div class="brand">
    <div class="brand-dot"></div>
    <div class="brand-name">BOREALIS<span>Energy Services Corp.</span></div>
  </div>

  <div class="contact">
    <h1 class="contact-name">DANIEL MOORE</h1>
    <p class="contact-role">CEO/Founder</p>
    <p class="contact-address">4120 Cedar Ridge Road<br>Anchorage, Alaska 99501</p>
    <ul class="contact-list">
      <li><svg viewBox="0 0 16 16"><path d="M3 1l3 3-1.5 2c1 2 3 4 5 5L11.5 9.5l3 3-2 2.5C7 14.5 1.5 9 1 3z"/></svg>555 210 4417</li>
      <li><svg viewBox="0 0 16 16"><path d="M4 0h8v16H4z M5.5 2v10h5V2z"/></svg>555 318 7720</li>
      <li><svg viewBox="0 0 16 16"><path d="M4 1h8v4H4z M1 6h14v7H1z M4 10h8v5H4z"/></svg>555 402 1186</li>
      <li><svg viewBox="0 0 16 16"><path d="M1 3h14v10H1z" fill="var(--navy)"/><path d="M1.5 3.5L8 9l6.5-5.5" stroke="#fff" stroke-width="1.3" fill="none"/></svg>daniel@borealisenergy.com</li>
      <li><svg viewBox="0 0 16 16"><circle cx="8" cy="8" r="7"/><path d="M4 5c2 0 2 2 4 2s1 3-1 4M10 2c0 2 3 2 4 4" stroke="#fff" stroke-width="1.3" fill="none"/></svg><span class="web">www.borealisenergy.com</span></li>
    </ul>
  </div>
</section>

<section class="card card-back">
  <svg class="card-art" viewBox="0 0 615 352">
    <defs>
      <radialGradient id="siteGlow" cx="0.55" cy="0.48" r="0.6">
        <stop offset="0" stop-color="#b3aa86"/>
        <stop offset="0.45" stop-color="#6b6650"/>
        <stop offset="0.8" stop-color="#1c1c16"/>
        <stop offset="1" stop-color="#050505"/>
      </radialGradient>
      <linearGradient id="edgeFade" x1="0" x2="1">
        <stop offset="0" stop-color="#000" stop-opacity="1"/>
        <stop offset="1" stop-color="#000" stop-opacity="0"/>
      </linearGradient>
    </defs>
    <rect x="150" y="0" width="465" height="352" fill="url(#siteGlow)" role="img" aria-label="Aerial night photograph of an illuminated drilling rig site"/>
    <rect x="150" y="0" width="60" height="352" fill="url(#edgeFade)"/>
    <circle cx="80" cy="262" r="30" fill="var(--lime)"/>
    <text transform="translate(100,192) rotate(-90)" fill="var(--lime)" font-family="Open Sans, Arial, sans-serif" font-weight="600" font-size="32" letter-spacing="0.5">BOREALIS</text>
    <text transform="translate(120,192) rotate(-90)" fill="var(--lime)" font-family="Open Sans, Arial, sans-serif" font-weight="600" font-size="14">Energy Services Corp.</text>
    <text transform="translate(160,322) rotate(-90)" fill="var(--white)" font-family="Open Sans, Arial, sans-serif" font-style="italic" font-weight="700" font-size="20">Leading every crew home SAFE</text>
  </svg>
</section>

</body>
</html>
```